Printing company needs stellar web site!

We need a website for a printing company based in Atlanta, Georgia, USA. Our company is 26 years old and just this year did a logo and branding refresh. Now we need our website to be refreshed as well.

Please see the attached source files for our new logo and stationary design.

Printing

```html
<!DOCTYPE html>
<html lang="en">
<head>
<meta charset="utf-8">
<title>Larkhaven – Home</title>
<link href="https://fonts.googleapis.com/css2?family=Cabin:wght@400;500;600;700&family=Oxanium:wght@500;600&display=swap" rel="stylesheet">
<style>
  :root {
    --page-top: #e4e7ea;
    --page-mid: #eef0f2;
    --page-bottom: #f3f4f6;
    --streak: rgba(255,255,255,0.55);
    --ink: #1b1b1b;
    --body-ink: #2b2b2b;
    --teal-light: #45c9d4;
    --teal: #2bb0bd;
    --nav-dark-top: #3a3a3a;
    --nav-dark-bottom: #161616;
    --nav-divider: #ffffff;
    --search-border: #cfd3d6;
    --search-text: #8a8f93;
    --dot-idle: #a9acaf;
    --photo-light: #efe9e4;
    --photo-mid: #c79a7c;
    --photo-dark: #6e4630;
  }
  * { box-sizing: border-box; margin: 0; padding: 0; }
  html, body { width: 1200px; height: 750px; overflow: hidden; }
  body {
    font-family: "Cabin", Arial, sans-serif;
    background:
      linear-gradient(150deg, transparent 0 38%, var(--streak) 39%, transparent 46%),
      linear-gradient(160deg, transparent 0 20%, rgba(255,255,255,0.35) 22%, transparent 30%),
      linear-gradient(180deg, var(--page-top), var(--page-mid) 50%, var(--page-bottom));
    color: var(--ink);
  }
  .site { position: relative; width: 940px; height: 750px; margin: 0 auto; }

  .brand {
    position: absolute; left: 6px; top: 66px;
    display: flex; align-items: center; gap: 14px;
  }
  .brand-dot { width: 60px; height: 60px; border-radius: 50%; background: var(--ink); }
  .brand-name { font-family: "Cabin", Arial, sans-serif; font-weight: 700; font-size: 46px; line-height: 1; color: var(--ink); }

  .site-search {
    position: absolute; right: 0; top: 31px;
    width: 186px; height: 33px; border-radius: 17px;
    border: 1px solid var(--search-border); background: #fff;
    display: flex; align-items: center; justify-content: space-between;
    padding: 0 2px 0 18px;
  }
  .site-search span { font-size: 12px; color: var(--search-text); letter-spacing: .3px; }
  .search-button { width: 27px; height: 27px; border-radius: 50%; background: var(--teal); display: flex; align-items: center; justify-content: center; }

  .main-nav {
    position: absolute; left: 0; top: 216px; width: 940px; height: 62px;
    display: flex; gap: 2px; border-radius: 10px; overflow: hidden;
    background: var(--nav-divider);
  }
  .main-nav a {
    flex: 1; display: flex; align-items: center; justify-content: center;
    color: #fff; text-decoration: none; font-size: 15px; font-weight: 500;
    background: linear-gradient(180deg, var(--nav-dark-top), var(--nav-dark-bottom));
  }
  .main-nav a.is-active { background: linear-gradient(180deg, var(--teal-light), var(--teal)); }

  .hero-photo {
    position: absolute; left: 528px; top: 278px; width: 412px; height: 472px;
    background:
      radial-gradient(ellipse 38% 40% at 48% 40%, var(--photo-mid), transparent 75%),
      radial-gradient(ellipse 55% 60% at 50% 45%, var(--photo-dark), transparent 80%),
      linear-gradient(180deg, transparent 70%, var(--photo-light) 90%);
  }

  .hero-copy { position: absolute; left: 0; top: 376px; width: 440px; }
  .hero-title {
    font-family: "Oxanium", "Arial Narrow", sans-serif; font-weight: 500;
    font-size: 44px; line-height: 38px; letter-spacing: .5px; color: var(--ink);
  }
  .hero-text { margin-top: 18px; font-size: 14px; line-height: 24px; font-weight: 600; color: var(--body-ink); white-space: nowrap; }
  .read-more {
    display: inline-flex; align-items: center; justify-content: center;
    margin-top: 20px; width: 112px; height: 40px; border-radius: 12px;
    background: linear-gradient(180deg, var(--teal-light), var(--teal));
    color: #fff; font-size: 14px; text-decoration: none;
  }
  .slider-dots { position: absolute; left: 3px; top: 641px; display: flex; gap: 6px; }
  .slider-dots i { width: 14px; height: 14px; border-radius: 50%; background: var(--dot-idle); }
  .slider-dots i.is-current { background: var(--teal); }
</style>
</head>
<body>
  <div class="site">
    <div class="brand">
      <span class="brand-dot"></span>
      <span class="brand-name">Larkhaven</span>
    </div>

    <div class="site-search">
      <span>SITE SEARCH</span>
      <span class="search-button">
        <svg width="15" height="15" viewBox="0 0 16 16" aria-hidden="true">
          <circle cx="6.5" cy="6.5" r="4.5" fill="none" stroke="#fff" stroke-width="2"/>
          <line x1="10" y1="10" x2="14" y2="14" stroke="#fff" stroke-width="2.4" stroke-linecap="round"/>
        </svg>
      </span>
    </div>

    <nav class="main-nav">
      <a href="#" class="is-active">HOME</a>
      <a href="#">ABOUT</a>
      <a href="#">SERVICES</a>
      <a href="#">CLIENTS</a>
      <a href="#">RESOURCES</a>
      <a href="#">FTP</a>
      <a href="#">CONTACT</a>
    </nav>

    <div class="hero-photo" role="img" aria-label="Smiling customer service agent wearing a headset"></div>

    <section class="hero-copy">
      <h1 class="hero-title">MULTIPLE<br>DEMANDS.<br>ONE SOLUTION.</h1>
      <p class="hero-text">Larkhaven is a one source provider of Commercial Printing,<br>Corporate Apparel, and Fulfillment Services.</p>
      <a href="#" class="read-more">READ MORE</a>
    </section>

    <div class="slider-dots"><i></i><i class="is-current"></i></div>
  </div>
</body>
</html>
```